Banner Ad to promote Youth Cycling Camps

We need a 728 x 90 banner ad to promote some youth cycling camps. There are 2 different camps - a road camp where they learn to ride their bikes on the roads and a mountain bike camp. The camps teach bike handling skills and racing tactics.

Target Market(s)

Parents of youth ages 7-17

Industry/Entity Type

Non-Profit

Font styles to use
Sans Serif

Requirements
Must have
• Logo
• Dates - Road Camp May 5-7, 2017
• - Mountain Bike Camp July 14-16, 2017
• website - pedalwaycircuit.org
• be 728 x 90
Nice to have
• Animated - would like it to rotate with 3 slides - 1 a focus on both camps, 1 on road camp, 1 on mountain bike camp

```html
<!DOCTYPE html>
<html lang="en">
<head>
<meta charset="utf-8">
<title>Banner Ad – Youth Cycling Camps</title>
<link rel="stylesheet" href="https://fonts.googleapis.com/css2?family=Montserrat:wght@500;600;800&family=Roboto+Slab:wght@400&display=swap">
<style>
  :root {
    --bg-dark: #0b0b0b;
    --bg-mid: #1a1a1a;
    --label-grey: #9a9a9a;
    --brand-blue: #1e9cf0;
    --brand-navy: #0d1f3a;
    --headline-yellow: #fde93a;
    --accent-pink: #e6137f;
    --text-white: #ffffff;
    --outline-dark: #1b1b1b;
  }
  * { box-sizing: border-box; margin: 0; padding: 0; }
  html, body { width: 1200px; height: 874px; overflow: hidden; }
  body {
    position: relative;
    background: linear-gradient(90deg, var(--bg-dark) 0%, var(--bg-mid) 25%, #111 50%, var(--bg-mid) 75%, var(--bg-dark) 100%);
    font-family: "Montserrat", Arial, sans-serif;
  }
  .presentation-title, .frame-label {
    position: absolute; left: 0; width: 100%;
    text-align: center;
    font-family: "Roboto Slab", Georgia, serif;
    font-weight: 400;
    color: var(--label-grey);
    line-height: 1;
  }
  .presentation-title { top: 94px; font-size: 23px; }
  .frame-label { font-size: 23px; }
  .frame-label.f1 { top: 174px; }
  .frame-label.f2 { top: 350px; }
  .frame-label.f3 { top: 530px; }

  .banner {
    position: absolute; left: 204px; width: 794px; height: 96px;
    overflow: hidden; background: #222;
  }
  .banner.f1 { top: 215px; }
  .banner.f2 { top: 390px; }
  .banner.f3 { top: 572px; }

  .brand-panel {
    position: absolute; left: 0; top: 0; width: 107px; height: 96px;
    background: var(--brand-blue); z-index: 3;
    display: flex; flex-direction: column; align-items: center; justify-content: center; gap: 5px;
  }
  .brand-panel::after {
    content: ""; position: absolute; right: -10px; top: 38px;
    border-top: 10px solid transparent; border-bottom: 10px solid transparent;
    border-left: 10px solid var(--brand-blue);
  }
  .brand-dot { width: 22px; height: 22px; border-radius: 50%; background: var(--brand-navy); }
  .brand-name {
    color: var(--brand-navy); font-weight: 800; font-size: 12px;
    line-height: 1.15; text-align: center; letter-spacing: .5px;
  }

  .photo { position: absolute; left: 107px; top: 0; right: 0; bottom: 0; z-index: 1; }
  .photo.young-rider { background: linear-gradient(90deg, #2b3140 0%, #4d5a3c 35%, #5f6d44 60%, #4b5e3a 80%, #34452e 100%); }
  .photo.road-group { background: linear-gradient(90deg, #1d2a1f 0%, #2f4030 30%, #6b7a6a 55%, #3d5238 80%, #243626 100%); }
  .photo.mtb-group { background: linear-gradient(90deg, #1f2a18 0%, #4a5b3a 35%, #7c95a8 60%, #6d8aa0 80%, #3e5560 100%); }

  .copy { position: absolute; z-index: 2; }
  .headline {
    color: var(--headline-yellow); font-weight: 800; text-transform: uppercase;
    text-shadow: 2px 2px 0 var(--outline-dark); white-space: nowrap;
  }
  .f1 .copy.main { left: 258px; top: 7px; width: 310px; text-align: center; }
  .f1 .headline { font-size: 20px; line-height: 23px; letter-spacing: -0.3px; }
  .f1 .tagline {
    color: var(--text-white); font-weight: 600; font-size: 12px; line-height: 15px;
    margin-top: 2px; white-space: nowrap; text-shadow: 1px 1px 0 var(--outline-dark);
  }

  .age-badge {
    position: absolute; z-index: 2; left: 558px; top: 14px; width: 68px; height: 68px;
    border-radius: 50%; background: var(--accent-pink); border: 3px solid #fff06a;
    display: flex; flex-direction: column; align-items: center; justify-content: center;
    color: var(--headline-yellow); font-weight: 800; font-size: 13px; line-height: 14px;
  }

  .f2 .copy.main { left: 138px; top: 29px; }
  .f2 .headline { font-size: 31px; line-height: 38px; }
  .f3 .copy.main { left: 138px; top: 17px; }
  .f3 .headline { font-size: 31px; line-height: 31px; }

  .copy.details { left: 598px; top: 21px; }
  .event-date { color: var(--text-white); font-weight: 600; font-size: 21px; line-height: 26px; white-space: nowrap; }
  .web-address {
    display: inline-block; margin-top: 6px; width: 159px; padding: 3px 0;
    text-align: center; font-size: 15px; font-weight: 500; white-space: nowrap;
  }
  .web-address.yellow { background: var(--headline-yellow); color: var(--outline-dark); }
  .web-address.pink { background: var(--accent-pink); color: var(--text-white); }
</style>
</head>
<body>
  <h1 class="presentation-title">Banner Ad to promote Youth Cycling Camps</h1>

  <h2 class="frame-label f1">Frame - 1</h2>
  <section class="banner f1">
    <div class="brand-panel"><span class="brand-dot"></span><span class="brand-name">PEDALWAY<br>CIRCUIT</span></div>
    <div class="photo young-rider" role="img" aria-label="Young cyclist in a helmet on the left and a youth rider with a coach on mountain bikes on the right"></div>
    <div class="copy main">
      <p class="headline">Best cycling camps<br>for youth</p>
      <p class="tagline">Professional Coaches,<br>Great youth to adult ratio, Affordable</p>
    </div>
    <div class="age-badge"><span>AGES</span><span>7-17</span></div>
  </section>

  <h2 class="frame-label f2">Frame - 2</h2>
  <section class="banner f2">
    <div class="brand-panel"><span class="brand-dot"></span><span class="brand-name">PEDALWAY<br>CIRCUIT</span></div>
    <div class="photo road-group" role="img" aria-label="Group of road cyclists riding together along a forest road"></div>
    <div class="copy main"><p class="headline">Road Camp</p></div>
    <div class="copy details">
      <p class="event-date">May 5-7, 2017</p>
      <p class="web-address yellow">pedalwaycircuit.org</p>
    </div>
  </section>

  <h2 class="frame-label f3">Frame - 3</h2>
  <section class="banner f3">
    <div class="brand-panel"><span class="brand-dot"></span><span class="brand-name">PEDALWAY<br>CIRCUIT</span></div>
    <div class="photo mtb-group" role="img" aria-label="Group of mountain bike campers and coaches posing among pine trees"></div>
    <div class="copy main"><p class="headline">Mountain<br>Bike Camp</p></div>
    <div class="copy details">
      <p class="event-date">July 14-16, 2017</p>
      <p class="web-address pink">pedalwaycircuit.org</p>
    </div>
  </section>
</body>
</html>
```